Ridgely Forge business card for handing simple contact information and generating service awareness

Utilizing the attached logo(s), generate a professional, but approachable, card conveying a sense of capability and integrity. Please only use one logo of the four attached; the different colors are all acceptable, but preference will be given to a design integrating a teal/turquoise logo,

I do not know where to put in the contact information or details?

Target Market(s)

Agriculture, Farming, Timber, Forestry, Construction, Crane Service

Industry/Entity Type

Contact Information for Business Card

Name, Phone Number, email address

Colors

Designer to choose colors to be used in the design.

Requirements
Nice to have
• It would be great to have either a mountain or one of the attached cranes as a backdrop on the rear of the card. Simple watermarks and/or Debossing is also great

```html
<!DOCTYPE html>
<html lang="en">
<head>
<meta charset="utf-8">
<title>Ridgely Forge – Business Card</title>
<link rel="stylesheet" href="https://fonts.googleapis.com/css2?family=Montserrat:wght@400;500;700;800&display=swap">
<style>
  :root {
    --teal: #286f63;
    --white: #ffffff;
    --ink: #222222;
    --backdrop: #3a3a3a;
  }
  * { margin: 0; padding: 0; box-sizing: border-box; }
  html, body { width: 1200px; height: 1059px; overflow: hidden; }
  body {
    background: var(--backdrop);
    font-family: "Montserrat", sans-serif;
    position: relative;
  }
  .card {
    position: absolute;
    border-radius: 18px;
    overflow: hidden;
  }
  .card-front { left: 256px; top: 100px; width: 688px; height: 391px; background: var(--white); }
  .card-back { left: 253px; top: 537px; width: 694px; height: 394px; background: var(--teal); }

  .brand { position: absolute; display: flex; flex-direction: column; align-items: center; }
  .brand-front { left: 430px; top: 30px; width: 230px; }
  .brand-back { left: 0; top: 105px; width: 100%; }
  .brand-mark { border-radius: 50%; }
  .brand-front .brand-mark { width: 96px; height: 96px; background: var(--teal); }
  .brand-back .brand-mark { width: 150px; height: 150px; background: var(--white); }
  .brand-name { font-weight: 800; text-transform: uppercase; white-space: nowrap; }
  .brand-front .brand-name { color: var(--teal); font-size: 25px; margin-top: 18px; }
  .brand-back .brand-name { color: var(--white); font-size: 42px; margin-top: 26px; }

  .name-bar { position: absolute; left: 0; top: 183px; width: 18px; height: 46px; background: var(--teal); }
  .person-name {
    position: absolute; left: 31px; top: 178px;
    font-size: 30px; font-weight: 700; color: var(--teal); letter-spacing: 0.5px;
  }
  .person-role {
    position: absolute; left: 31px; top: 214px;
    font-size: 16px; font-weight: 400; color: var(--ink); letter-spacing: 0.5px;
  }
  .divider { position: absolute; left: 31px; top: 249px; width: 629px; height: 2px; background: var(--teal); }

  .contact-list { position: absolute; left: 31px; top: 266px; list-style: none; }
  .contact-list li {
    display: flex; align-items: center; height: 25px;
    font-size: 16px; color: var(--ink); letter-spacing: 0.3px;
  }
  .contact-list svg { width: 13px; height: 13px; margin-right: 8px; fill: var(--teal); flex: none; }

  .address {
    position: absolute; right: 28px; top: 320px; text-align: right;
    font-size: 16px; line-height: 21px; color: var(--ink); letter-spacing: 0.3px;
  }
</style>
</head>
<body>
  <section class="card card-front">
    <div class="brand brand-front">
      <div class="brand-mark"></div>
      <div class="brand-name">Ridgely Forge</div>
    </div>

    <div class="name-bar"></div>
    <h1 class="person-name">DORIAN VALE</h1>
    <p class="person-role">MANAGER</p>
    <div class="divider"></div>

    <ul class="contact-list">
      <li>
        <svg viewBox="0 0 16 16" aria-hidden="true"><path d="M3.5 1l2.5 3-1.5 1.6c.8 2 2.2 3.4 4.3 4.4L10.4 8.5l3.1 2.4-1.3 2.8c-5.4-.6-9.5-4.8-10-10.2z"/></svg>
        (555)210-4478
      </li>
      <li>
        <svg viewBox="0 0 16 16" aria-hidden="true"><path d="M4.5 0h7A1.5 1.5 0 0 1 13 1.5v13A1.5 1.5 0 0 1 11.5 16h-7A1.5 1.5 0 0 1 3 14.5v-13A1.5 1.5 0 0 1 4.5 0zM4.8 2v10h6.4V2zM8 12.8a1 1 0 1 0 0 2 1 1 0 0 0 0-2z"/></svg>
        (555)318-90521
      </li>
      <li>
        <svg viewBox="0 0 16 16" aria-hidden="true"><path d="M0 3h16v1.2L8 9 0 4.2zM0 5.8l8 4.8 8-4.8V13H0z"/></svg>
        hello@ridgelyforge.com
      </li>
      <li>
        <svg viewBox="0 0 16 16" aria-hidden="true"><path d="M8 0a8 8 0 1 0 0 16A8 8 0 0 0 8 0zm0 1.3c.9 0 1.9 1.8 2.2 4.7H5.8C6.1 3.1 7.1 1.3 8 1.3zM1.4 7.2h3.2v1.6H1.4zM5.8 7.2h4.4v1.6H5.8zM11.4 7.2h3.2v1.6h-3.2zM5.8 10h4.4C9.9 12.9 8.9 14.7 8 14.7S6.1 12.9 5.8 10z"/></svg>
        www.ridgelyforge.com
      </li>
    </ul>

    <address class="address" style="font-style:normal">
      2214 North Pine Ridge Road<br>
      Cedar Falls, MN 55012
    </address>
  </section>

  <section class="card card-back">
    <div class="brand brand-back">
      <div class="brand-mark"></div>
      <div class="brand-name">Ridgely Forge</div>
    </div>
  </section>
</body>
</html>
```